Word Page Templates x 5

1 x Letterhead Template with Header and Footer able to be printed to paper and pdf with non blurry resolution
- File attached looks ok on computer screen but does not print the same
- We are wanting it to print like it looks on the screen
- We are wanting it to print not fuzzy in resolution
- We are wanting the banner to be on the absolute edge of the page like it is on the computer screen
- We are needing to print this to paper and pdf with perfect resolution and colour

Please can someone help us!!

I have provided the logo files in our posession. If better resolutions are required please let us know.

We are also wanting 4 simple page templates to be setup in Landscape and Portrait orientation as well once we are happy with the letterhead that is provided samples have been provided
Updates

Hi all I have the vector files available now along with a Colour profile

Requirements
Must have
• Clear when printed on A4 Paper
Should not have
• Blurry images, Colour must be correct (same as Logo) - Please reference our website if need be ..... vornal.com.au

```html
<!DOCTYPE html>
<html lang="en">
<head>
<meta charset="utf-8">
<title>Vornal Letterhead</title>
<link href="https://fonts.googleapis.com/css2?family=Montserrat:wght@500&display=swap" rel="stylesheet">
<style>
  :root {
    --page: #ffffff;
    --mint: #8ccfb6;
    --slate: #8a93b8;
    --ink: #7c88a8;
    --label: #79c2a8;
  }
  html, body {
    margin: 0;
    padding: 0;
    width: 849px;
    height: 1200px;
    overflow: hidden;
    background: var(--page);
  }
  .letterhead {
    position: relative;
    width: 849px;
    height: 1200px;
    background: var(--page);
    font-family: "Montserrat", Arial, sans-serif;
  }
  .edge-band {
    position: absolute;
    left: 0;
    width: 849px;
    height: 20px;
    background: linear-gradient(90deg, var(--mint), var(--slate));
    opacity: 0.85;
  }
  .edge-band--top { top: 8px; }
  .edge-band--bottom { top: 1168px; }
  .brand-name {
    position: absolute;
    left: 44px;
    top: 88px;
    margin: 0;
    font-weight: 500;
    font-size: 44px;
    line-height: 1;
    color: var(--ink);
  }
  .contact-list {
    position: absolute;
    left: 582px;
    top: 74px;
    margin: 0;
    padding: 0;
    list-style: none;
    font-weight: 500;
    font-size: 12px;
    line-height: 21px;
    color: var(--ink);
  }
  .contact-list .label {
    color: var(--label);
    margin-right: 4px;
  }
</style>
</head>
<body>
<main class="letterhead">
  <div class="edge-band edge-band--top" role="img" aria-label="Decorative border band along the top edge in mint to slate tones"></div>

  <h1 class="brand-name">Vornal</h1>

  <ul class="contact-list">
    <li><span class="label">A.</span>PO Box 2810, Kallow QLD 4021</li>
    <li><span class="label">P.</span>07 3000 4127</li>
    <li><span class="label">E.</span>admin@vornal.com.au</li>
    <li><span class="label">W.</span>www.vornal.com.au</li>
  </ul>

  <div class="edge-band edge-band--bottom" role="img" aria-label="Decorative border band along the bottom edge in mint to slate tones"></div>
</main>
</body>
</html>
```